International Petrochemical business needs a web design for Tessaro Desk system

We need a web design for a "Tessaro Desk" system for an international petrochemical company. The web site is used internally within the company. It is hosted by an internal department which provides government permit request service for other departments.

We would like to see designs of two pages using color light blue. (home page, internal page as attached).
Home Page:
1. Header has a background image and small animation. Header on home page can be taller than the header of the internal page.
2. Layout as attached.

Internal Page:
1. Header can use the same background image as the home page and can be shorter to utilize the page for content.
2. The blue icon behind every captions represent an icon. When user move mouse over this icon, it displays the caption in Thai language as a tooltip. This icon needs to be redesign.

The final design should communicate the followings:
- Excellent service provided system in terms of time and accurary
- Rapid growth of business via building petrochemical refinery plant

For Internal Page, the blue circle behind every captions represent an icon. When mouse over this icon, a tool tip showing the caption in Thai language is shown. Please also design this icon..

There are more feedbacks from customer as followed:

1. Banner should consists of 
    1.1 "Approved" stamp on paper
    1.2 An image of Garuda. It is used on every government documents in Thailand
    1.3 Image of petrochemical plant
2. Each menu item (Home, Permit, Search, etc) should have different colors. Drop down menu will use the same color as its parent menu item.
3. Overall tone of the web page should be light blue with background of the body the web page in white
4. "New Request" button should use green color with icon on it
5. Table header of each box in the body of the page should use dark blue background with text in white

Please kindly submit your revisions.
Thank you.

Reason: We get some late feedbacks from customers which was just updated to all designers.

• 1. Design for 1024x768 screen resolution
2. Use light blue theme
3. Background of header where the company logo is must have white background

```html
<!DOCTYPE html>
<html lang="en">
<head>
<meta charset="utf-8">
<title>Tessaro Desk – Home</title>
<link rel="stylesheet" href="https://fonts.googleapis.com/css2?family=Montserrat:wght@800&family=Noto+Sans:wght@400;700&display=swap">
<style>
:root{
  --blue:#72a8d1;
  --teal:#5ecdbf;
  --coral:#f37370;
  --panel:#f0f0ee;
  --rule:#dcdcda;
  --ink:#333;
  --head-ink:#2b3035;
  --muted:#8a8a8a;
  --banner:#000;
  --white:#fff;
}
*{box-sizing:border-box;margin:0;padding:0}
html,body{width:1200px;height:1147px;overflow:hidden;background:var(--white)}
body{position:relative;font-family:"Noto Sans",Verdana,sans-serif;color:var(--ink);font-size:11px}
.abs{position:absolute}
.top-strip{left:0;top:0;width:1200px;height:6px;background:var(--blue)}
.login{left:878px;top:0;width:132px;height:37px;background:var(--blue);color:var(--white);font-size:12.5px;display:flex;align-items:center;justify-content:center}
.brand{left:191px;top:64px;display:flex;align-items:center;gap:6px;font-weight:700;font-size:14px;color:var(--blue)}
.brand-dot{width:22px;height:22px;border-radius:50%;background:var(--blue)}
.help{left:877px;top:77px;font-size:11px;color:var(--ink);line-height:15px}
.help b{display:block;color:var(--blue);font-weight:700;letter-spacing:.3px}
.nav{left:0;top:143px;width:1200px;height:63px;background:var(--panel)}
.nav-item{top:0;height:63px;display:flex;align-items:center;justify-content:center;font-size:12.5px;color:#555;transform:translateX(-50%)}
.nav-item.active{background:var(--blue);color:var(--white);width:73px}
.dropdown{left:403px;top:206px;width:153px;height:103px;background:var(--blue);z-index:2;padding:17px 0 0 13px}
.dropdown span{display:block;color:var(--white);font-size:12.5px;line-height:24px}
.banner{left:0;top:206px;width:1200px;height:187px;background:var(--banner)}
.panel{background:var(--panel)}
.panel-title{height:34px;padding-left:25px;display:flex;align-items:center;font-family:Montserrat,sans-serif;font-weight:800;font-size:13.5px;letter-spacing:.3px;color:var(--head-ink)}
.t-blue{background:var(--blue)}
.t-teal{background:var(--teal)}
.t-coral{background:var(--coral)}
.row{position:relative;border-bottom:1px solid var(--rule)}
.row.head{font-size:11px}
.cell{position:absolute;top:50%;transform:translateY(-50%);white-space:nowrap}
.cell.c{transform:translate(-50%,-50%)}
.pager{position:relative;font-size:9.5px;color:var(--ink)}
.pager span{position:absolute;top:50%;left:50%;transform:translate(-50%,-50%);word-spacing:3px;white-space:nowrap}
.dot{display:inline-block;width:11px;height:11px;border-radius:50%;background:radial-gradient(circle at 35% 30%,#9a9a9a,#3a3a3a 70%);margin-left:9px;vertical-align:-1px}
.footer-box{left:192px;top:1109px;width:132px;height:36px;background:#a8a8a8;color:var(--white);font-size:11px;display:flex;align-items:center;justify-content:center}
.footer-line{left:192px;top:1141px;width:1008px;height:6px;background:#c4c4c4}
.footer-links{left:404px;top:1118px;font-size:11px;color:#9a9a9a;word-spacing:2px;white-space:pre}
</style>
</head>
<body>
<div class="abs top-strip"></div>
<div class="abs login">User Login</div>
<div class="abs brand"><span class="brand-dot"></span>Norvale Chemical</div>
<div class="abs help">Need Help !<b>+1 (800) 555 0142</b></div>

<nav class="abs nav">
  <span class="abs nav-item" style="left:333px">Home</span>
  <span class="abs nav-item active" style="left:440px">Permits</span>
  <span class="abs nav-item" style="left:553px">Search</span>
  <span class="abs nav-item" style="left:663px">Report</span>
  <span class="abs nav-item" style="left:770px">Admin</span>
  <span class="abs nav-item" style="left:870px">Help</span>
</nav>
<div class="abs dropdown"><span>Create New Permit</span><span>Transfer Role</span><span>Transfer Res. Person</span></div>
<div class="abs banner" role="img" aria-label="Header banner: approved permit stamp, national emblem and petrochemical plant"></div>

<section class="abs panel" style="left:191px;top:429px;width:389px;height:166px">
  <div class="panel-title t-blue">NEW REQUEST</div>
  <div class="row head" style="height:31px"><span class="cell" style="left:25px">REQUEST #</span><span class="cell c" style="left:185px">REQUESTED DATE</span><span class="cell c" style="left:327px">BRANCH</span></div>
  <div class="row" style="height:34px"><span class="cell" style="left:25px">56-003</span><span class="cell c" style="left:185px">20/4/2013</span><span class="cell c" style="left:325px">GC1</span></div>
  <div class="row" style="height:34px"><span class="cell" style="left:25px">56-004</span><span class="cell c" style="left:185px">21/4/2013</span><span class="cell c" style="left:325px">GC2</span></div>
  <div class="pager" style="height:32px"><span>&lt; &nbsp; 1 | 2 | 3 | 4 &nbsp; &gt;</span></div>
</section>

<section class="abs panel" style="left:622px;top:429px;width:388px;height:166px">
  <div class="panel-title t-teal">MY WORKING REQUESTS</div>
  <div class="row head" style="height:31px"><span class="cell" style="left:25px">REQUEST #</span><span class="cell c" style="left:202px">REQUESTED DATE</span><span class="cell c" style="left:343px">STATUS</span></div>
  <div class="row" style="height:34px"><span class="cell" style="left:25px">56-003</span><span class="cell c" style="left:202px">20/4/2013</span><span class="cell c" style="left:343px">Waiting</span></div>
  <div class="row" style="height:34px"><span class="cell" style="left:25px">56-004</span><span class="cell c" style="left:202px">21/4/2013</span><span class="cell c" style="left:351px">In progress</span></div>
  <div class="pager" style="height:32px"><span>&lt; &nbsp; 1 | 2 | 3 | 4 &nbsp; &gt;</span></div>
</section>

<section class="abs panel" style="left:191px;top:630px;width:820px;height:209px">
  <div class="panel-title t-coral">EXPIRING PERMITS</div>
  <div class="row head" style="height:52px"><span class="cell" style="left:29px">PERMIT NO.</span><span class="cell c" style="left:211px">EXPIRE DATE</span><span class="cell c" style="left:353px">PERMIT NAME</span><span class="cell c" style="left:482px">BRANCH</span><span class="cell c" style="left:613px">REQUIRED(DAY)</span><span class="cell c" style="left:763px">DUE DATE</span></div>
  <div class="row" style="height:35px"><span class="cell" style="left:30px">AB56001</span><span class="cell c" style="left:211px">25/3/2013</span><span class="cell c" style="left:352px">Permit Name ###10</span><span class="cell c" style="left:481px">GC1</span><span class="cell" style="left:590px">30<i class="dot"></i></span><span class="cell c" style="left:760px">-40</span></div>
  <div class="row" style="height:34px"><span class="cell" style="left:30px">AB56001</span><span class="cell c" style="left:211px">25/3/2013</span><span class="cell c" style="left:352px">Permit Name ###10</span><span class="cell c" style="left:481px">GC1</span><span class="cell" style="left:590px">30<i class="dot"></i></span><span class="cell c" style="left:760px">-40</span></div>
  <div class="pager" style="height:54px"><span style="left:408px">&lt; &nbsp; 1 | 2 | 3 | 4 &nbsp; &gt;</span></div>
</section>

<section class="abs panel" style="left:191px;top:874px;width:389px;height:166px">
  <div class="panel-title t-blue">MY IN PROGRESS REQUESTS</div>
  <div class="row head" style="height:31px"><span class="cell" style="left:25px">REQUEST #</span><span class="cell c" style="left:185px">REQUESTED DATE</span><span class="cell c" style="left:344px">STATUS</span></div>
  <div class="row" style="height:34px"><span class="cell" style="left:25px">56-0001</span><span class="cell c" style="left:185px">20/4/2013</span><span class="cell c" style="left:342px">GC1</span></div>
  <div class="row" style="height:34px"><span class="cell" style="left:25px">56-004</span><span class="cell c" style="left:185px">21/4/2013</span><span class="cell c" style="left:341px">GC2</span></div>
  <div class="pager" style="height:32px"><span style="left:180px">&lt; &nbsp; 1 | 2 | 3 | 4 &nbsp; &gt;</span></div>
</section>

<section class="abs panel" style="left:622px;top:874px;width:388px;height:166px">
  <div class="panel-title t-blue">MY IN PROGRESS REQUESTS</div>
  <div class="row head" style="height:31px"><span class="cell" style="left:42px">REQUEST #</span><span class="cell c" style="left:203px">REQUESTED DATE</span><span class="cell c" style="left:343px">STATUS</span></div>
  <div class="row" style="height:34px"><span class="cell" style="left:42px">56-0001</span><span class="cell c" style="left:203px">20/4/2013</span><span class="cell c" style="left:342px">GC1</span></div>
  <div class="row" style="height:34px"><span class="cell" style="left:42px">56-004</span><span class="cell c" style="left:203px">21/4/2013</span><span class="cell c" style="left:341px">GC2</span></div>
  <div class="pager" style="height:32px"><span style="left:180px">&lt; &nbsp; 1 | 2 | 3 | 4 &nbsp; &gt;</span></div>
</section>

<footer>
  <div class="abs footer-line"></div>
  <div class="abs footer-box">Copyright © 2013</div>
  <div class="abs footer-links">Home    |    Permits    |    Search    |      Report   |    Admin   |   Help</div>
</footer>
</body>
</html>
```